Modern Design Business Card industrial maintenance company

Business card design for Company named Brookvale Equipment Services

Target Market(s)

Industrial

Industry/Entity Type

Maintenance and repair

Contact Information for Business Card

Place holder for address, office phone, mobile number and email

Requirements
Must have
• Clean modern look
Nice to have
• N/a

```html
<!DOCTYPE html>
<html lang="en">
<head>
<meta charset="utf-8">
<title>Brookvale Equipment Services – Business Card</title>
<link href="https://fonts.googleapis.com/css2?family=Arimo:wght@400;700&display=swap" rel="stylesheet">
<style>
  :root {
    --backdrop: #1c1c1e;
    --card-light: #ffffff;
    --card-dark: #3a3a3a;
    --ink-dark: #1a1a1a;
    --ink-light: #ffffff;
    --ink-muted: #e4e4e4;
  }
  * { margin: 0; padding: 0; box-sizing: border-box; }
  html, body { width: 1200px; height: 874px; overflow: hidden; background: var(--backdrop); }
  body { font-family: "Arimo", Arial, sans-serif; position: relative; }

  .card {
    position: absolute;
    left: 290px;
    width: 620px;
    height: 354px;
    border-radius: 22px;
    overflow: hidden;
  }

  /* Front */
  .card-front { top: 60px; background: var(--card-light); }
  .front-brand {
    position: absolute; inset: 0;
    display: flex; align-items: center; justify-content: center; gap: 22px;
  }
  .brand-circle {
    width: 78px; height: 78px; border-radius: 50%;
    border: 6px solid var(--ink-dark); flex: none;
  }
  .brand-name {
    color: var(--ink-dark); font-weight: 700; font-size: 34px;
    line-height: 1.1; letter-spacing: 2px; text-transform: uppercase;
  }

  /* Back */
  .card-back { top: 460px; background: var(--card-dark); color: var(--ink-light); }
  .back-brand {
    position: absolute; left: 44px; top: 34px;
    font-weight: 700; font-size: 20px; letter-spacing: 1.6px;
    line-height: 1.15; text-transform: uppercase; color: var(--ink-light);
  }
  .person { position: absolute; left: 44px; top: 120px; }
  .person-name { font-weight: 700; font-size: 24px; }
  .person-role { font-size: 14px; color: var(--ink-muted); margin-top: 2px; }
  .address {
    position: absolute; left: 44px; top: 184px;
    font-size: 15px; line-height: 1.35; color: var(--ink-muted);
  }
  .contact-list {
    position: absolute; left: 44px; top: 240px; list-style: none;
    font-size: 15px; line-height: 1.45; color: var(--ink-muted);
  }
  .contact-list li { display: flex; align-items: center; gap: 8px; }
  .contact-list svg { width: 13px; height: 13px; fill: var(--ink-light); flex: none; }
  .back-circle {
    position: absolute; right: 44px; top: 42px;
    width: 270px; height: 270px; border-radius: 50%;
    border: 10px solid var(--ink-light);
  }
</style>
</head>
<body>
  <section class="card card-front">
    <div class="front-brand">
      <div class="brand-circle"></div>
      <div class="brand-name">Brookvale<br>Equipment Services</div>
    </div>
  </section>

  <section class="card card-back">
    <div class="back-brand">Brookvale<br>Equipment Services</div>
    <div class="person">
      <div class="person-name">Daniel Mercer</div>
      <div class="person-role">President</div>
    </div>
    <div class="address">412 Harbor Road<br>Riverton, Canada 20418</div>
    <ul class="contact-list">
      <li><svg viewBox="0 0 16 16"><path d="M3.5 1l2.5 3-1.5 1.8c.8 1.9 2.3 3.4 4.2 4.2L10.5 8.5l3 2.5-1.3 2.8C6.8 13.8 2.2 9.2 1 3.8z"/></svg>555-210-4821</li>
      <li><svg viewBox="0 0 16 16"><path d="M4.5 0h7a1.5 1.5 0 0 1 1.5 1.5v13a1.5 1.5 0 0 1-1.5 1.5h-7A1.5 1.5 0 0 1 3 14.5v-13A1.5 1.5 0 0 1 4.5 0zm.5 2v10h6V2z"/></svg>555-318-7740</li>
      <li><svg viewBox="0 0 16 16"><path d="M1 3h14v10H1zm1.5 1.3v.4L8 8.5l5.5-3.8v-.4z"/></svg>info@brookvale.com</li>
      <li><svg viewBox="0 0 16 16"><circle cx="8" cy="8" r="7"/></svg>www.brookvale.com</li>
    </ul>
    <div class="back-circle"></div>
  </section>
</body>
</html>
```